Fashion Design Business Card

I need a new business card designed for a new fashion company. I have attached what I have currently designed. I want it more feminine looking, the logo needs to be gold. I want it simple, feminine and stylish. Please give me some different ideas with the fonts.
Updates

I need to send the design we currently have, as we have worked out the logo.
You also need all of our details
Industry/Entity Type
Fashion
Look and feel
Each slider illustrates characteristics of the customer's brand and the style your logo design should communicate.

```html
<!DOCTYPE html>
<html lang="en">
<head>
<meta charset="utf-8">
<title>Mirela Hartwell – Business Card</title>
<link rel="stylesheet" href="https://fonts.googleapis.com/css2?family=Cinzel:wght@400&family=Cormorant+Garamond:wght@400;500&display=swap">
<style>
  :root {
    --page-bg: #dcdcdc;
    --card-bg: #f6f6f6;
    --card-shade: #e8e8e8;
    --ink: #4a4a4a;
    --ink-soft: #6d6d6d;
    --gold: #c99434;
    --label-ink: #a0641c;
  }
  * { margin: 0; padding: 0; box-sizing: border-box; }
  html, body { width: 1200px; height: 634px; overflow: hidden; }
  body { background: var(--page-bg); position: relative; font-family: "Cormorant Garamond", serif; }

  .card {
    position: absolute;
    top: 98px;
    width: 528px;
    height: 315px;
    border-radius: 14px;
    overflow: hidden;
    background: linear-gradient(160deg, var(--card-bg) 0%, var(--card-shade) 55%, var(--card-bg) 100%);
  }
  .card--front { left: 43px; }
  .card--back { left: 639px; }

  .brand-mark {
    position: absolute;
    border-radius: 50%;
    background: var(--gold);
  }
  .card--front .brand-mark { width: 120px; height: 120px; left: 204px; top: 62px; }
  .card--back .brand-mark { width: 64px; height: 64px; left: 64px; top: 34px; }

  .brand-name {
    position: absolute;
    font-family: "Cinzel", serif;
    font-weight: 400;
    color: var(--ink);
    letter-spacing: 0.32em;
    white-space: nowrap;
  }
  .card--front .brand-name { left: 0; right: 0; top: 208px; text-align: center; font-size: 19px; }
  .card--back .brand-name { left: 144px; top: 67px; font-size: 15px; }

  .role {
    position: absolute;
    left: 145px;
    top: 86px;
    font-size: 14px;
    letter-spacing: 0.3em;
    color: var(--ink-soft);
  }

  .contact {
    position: absolute;
    left: 81px;
    top: 224px;
    display: grid;
    grid-template-columns: 65px auto;
    font-size: 13px;
    line-height: 14.5px;
    letter-spacing: 0.16em;
  }
  .contact dt { color: var(--label-ink); text-transform: uppercase; font-family: "Cinzel", serif; font-size: 11px; }
  .contact dd { color: var(--ink); }

  .side-label {
    position: absolute;
    top: 459px;
    font-family: "Cinzel", serif;
    font-size: 14px;
    letter-spacing: 0.2em;
    color: #222;
  }
  .side-label--front { left: 68px; }
  .side-label--back { left: 639px; }
</style>
</head>
<body>
  <section class="card card--front">
    <div class="brand-mark" aria-hidden="true"></div>
    <h1 class="brand-name">Mirela Hartwell</h1>
  </section>

  <section class="card card--back">
    <div class="brand-mark" aria-hidden="true"></div>
    <h2 class="brand-name">Mirela Hartwell</h2>
    <p class="role">fashion designer</p>
    <dl class="contact">
      <dt>Ph</dt><dd>0400612734</dd>
      <dt>Email</dt><dd>mirela@mirelahartwell.com</dd>
      <dt>Web</dt><dd>www.mirelahartwell.com</dd>
    </dl>
  </section>

  <p class="side-label side-label--front">FRONT</p>
  <p class="side-label side-label--back">BACK</p>
</body>
</html>
```